Audio Tour Poster

I need a poster to show information on a audio tour ... walk ... bike etc ... the poster needs to be generic so that it could be used for several projects ... a space needs to be left to add a tour title and another area where a tri fold brochure can be placed for people to access ... the tri fold poster will be based on 8.5 x 14 inch legal size ...

The size of the final poster will be 18x 24 inches ... an example of a audio tour can be found at
http://trallexo.com/walk/568 or http://trallexo.com/walk/2507

Industry/Entity Type

Legal

```html
<!DOCTYPE html>
<html lang="en">
<head>
<meta charset="utf-8">
<title>Audio Tour Poster</title>
<link rel="stylesheet" href="https://fonts.googleapis.com/css2?family=Oswald:wght@600;700&family=Raleway:wght@100;200;500;800&family=Roboto+Condensed:wght@300&display=swap">
<style>
  :root {
    --ink: #0a0c0f;
    --white: #ffffff;
    --ghost: #b9bec5;
    --title-blue: #4a8fac;
    --band-blue: #4aa4cf;
    --band-soft: #a9d3e8;
    --rule: #5b6068;
    --photo-top: #16181c;
    --photo-mid: #121722;
    --photo-low: #0b0e14;
  }
  * { margin: 0; padding: 0; box-sizing: border-box; }
  html, body { width: 909px; height: 1200px; overflow: hidden; background: var(--ink); }
  .poster {
    position: relative;
    width: 909px;
    height: 1200px;
    background: var(--ink);
    overflow: hidden;
    color: var(--white);
  }
  .top-strip { position: absolute; left: 0; top: 0; width: 909px; height: 18px; background: #07080a; }

  .backdrop-photo {
    position: absolute; left: 0; top: 18px; width: 909px; height: 750px;
    background: linear-gradient(180deg, var(--photo-top) 0%, var(--photo-top) 40%, var(--photo-mid) 70%, var(--photo-low) 100%);
  }

  .company {
    position: absolute; top: 46px; width: 100%; text-align: center;
    font: 700 27px/1 "Oswald", sans-serif;
  }
  .presents {
    position: absolute; top: 106px; width: 100%; text-align: center;
    font: 200 27px/1 "Raleway", sans-serif; color: var(--ghost);
  }
  .rule { position: absolute; height: 1px; background: var(--rule); }
  .rule-top { left: 103px; top: 151px; width: 704px; }
  .title-box {
    position: absolute; left: 103px; top: 159px; width: 704px; height: 182px;
    background: var(--title-blue);
    display: flex; align-items: center; justify-content: center;
    font-size: 122px; line-height: 1; font-weight: normal;
  }
  .title-light { font-family: "Raleway", sans-serif; font-weight: 100; }
  .title-bold { font-family: "Raleway", sans-serif; font-weight: 800; text-shadow: 2px 3px 4px rgba(0,0,0,.35); }

  .walk-row {
    position: absolute; top: 348px; left: 103px; width: 704px;
    display: flex; align-items: center; gap: 14px;
  }
  .walk-row .line { flex: 1; height: 1px; background: var(--rule); }
  .walk-type { font: 700 36px/1.2 "Oswald", sans-serif; }

  .location {
    position: absolute; top: 441px; width: 100%; text-align: center;
    font-size: 45px; line-height: 1; font-family: "Raleway", sans-serif;
  }
  .location .thin { font-weight: 100; color: var(--ghost); }
  .location .strong { font-weight: 500; }

  .date-band {
    position: absolute; left: 0; top: 499px; width: 909px; height: 63px;
    background: var(--band-blue);
    font-family: "Raleway", sans-serif; font-size: 35px; line-height: 63px;
  }
  .date-band span { position: absolute; top: 0; }
  .month { left: 102px; font-weight: 500; text-shadow: 1px 2px 3px rgba(0,0,0,.3); }
  .day { left: 249px; font-weight: 200; color: var(--band-soft); }
  .from { left: 447px; font-weight: 800; letter-spacing: 25px; text-shadow: 1px 2px 3px rgba(0,0,0,.3); }
  .time { left: 672px; font-weight: 200; color: var(--band-soft); letter-spacing: 28px; }

  .details {
    position: absolute; top: 591px; left: 0; width: 909px; text-align: center;
    font: 300 22px/27px "Roboto Condensed", sans-serif;
  }
  .rule-base { left: 0; top: 768px; width: 909px; background: #3a3d43; }

  .brochure-slot {
    position: absolute; left: 101px; top: 802px; width: 707px; height: 353px;
    border: 2px solid var(--white); border-radius: 3px; background: #0b0d10;
    display: flex; align-items: center; justify-content: center;
    padding-top: 22px;
    font: 700 25px/1 "Oswald", sans-serif; letter-spacing: .3px;
  }
</style>
</head>
<body>
<main class="poster">
  <div class="top-strip"></div>
  <div class="backdrop-photo" role="img" aria-label="Night city street photograph with fine diagonal pinstripe texture above and blurred lights reflected on water below"></div>

  <h2 class="company">Company Name</h2>
  <p class="presents">PRESENTS</p>
  <div class="rule rule-top"></div>
  <h1 class="title-box"><span class="title-light">TOUR</span><span class="title-bold">TITLE</span></h1>

  <div class="walk-row"><span class="line"></span><span class="walk-type">Listening Walk</span><span class="line"></span></div>

  <p class="location"><span class="thin">CITY</span> <span class="strong">STREET</span></p>

  <div class="date-band">
    <span class="month">MONTH</span>
    <span class="day">00TH</span>
    <span class="from">FROM</span>
    <span class="time">0PM</span>
  </div>

  <div class="details">
    <p>Any other details</p>
    <p>Any other details</p>
    <p>Any other details</p>
  </div>
  <div class="rule rule-base"></div>

  <section class="brochure-slot">BROCHURE GOES HERE</section>
</main>
</body>
</html>
```